IT Consultancy Business Card Design Project

We are an IT consultancy that focuses on CRM, mobile and enterprise technology solutions.
We need a design that portraits our tenacity for innovation that exceeds our clients' expectations. We would like a design that is modern, clean and innovative.

Target Market(s)

Our target audiences are generally large corporates. These corporates typically come from conservative industries.

Industry/Entity Type

Business

Requirements
Must have
• At a minimum, the business card need to show:
1. company name, logo, Sydney and Melbourne addresses, phone number, 0412 738 205, email address, website address. (Details from our website www.korvanta.com.au)
2. we do CRM, Mobile & Enterprise Solutions
3. we are a Delvaro certified partner with delvaro partner logo with competencies in DV Pellucor CRM and DV Quillnest.

```html
<!DOCTYPE html>
<html lang="en">
<head>
<meta charset="utf-8">
<title>Korvanta Business Card</title>
<link rel="stylesheet" href="https://fonts.googleapis.com/css2?family=Nunito:wght@700;800&display=swap">
<style>
  :root {
    --page: #ffffff;
    --board: #d1d2d4;
    --board-edge: #3a3a3a;
    --card: #ffffff;
    --ink: #111111;
    --mark-grey: #5a5a5a;
    --badge: #8a8a8a;
  }
  * { margin: 0; padding: 0; box-sizing: border-box; }
  html, body {
    width: 1149px; height: 1200px; overflow: hidden;
    background: var(--page);
    font-family: "Nunito", Arial, sans-serif;
    color: var(--ink);
  }
  .canvas { position: relative; width: 1149px; height: 1200px; }
  .board {
    position: absolute; left: 0; top: 0;
    width: 1148px; height: 1125px;
    background: var(--board);
    border: 1px solid var(--board-edge);
  }
  .card {
    position: absolute; top: 210px;
    width: 336px; height: 686px;
    background: var(--card);
    overflow: hidden;
  }
  .card--front { left: 128px; text-align: center; }
  .card--back { left: 652px; width: 332px; }

  .front-line { position: absolute; left: 0; right: 0; line-height: 1; white-space: nowrap; }
  .company-name { top: 22px; font-size: 31px; font-weight: 800; letter-spacing: -0.5px; }
  .tagline { top: 60px; font-size: 17px; font-weight: 700; }

  .brand-block {
    position: absolute; left: 0; right: 0; top: 95px; height: 220px;
    display: flex; flex-direction: column; align-items: center; justify-content: center; gap: 18px;
  }
  .brand-square { width: 62px; height: 62px; background: var(--ink); }
  .brand-name { font-size: 44px; font-weight: 800; line-height: 1; letter-spacing: -1px; }

  .partner {
    position: absolute; left: 0; right: 0; top: 326px;
    display: flex; align-items: center; justify-content: center; gap: 10px;
    font-size: 15px; font-weight: 800; line-height: 1; white-space: nowrap;
  }
  .partner-badge { width: 24px; height: 24px; background: var(--badge); }
  .competencies { top: 360px; font-size: 14px; font-weight: 700; }

  .website { top: 396px; font-size: 29px; font-weight: 800; letter-spacing: -0.5px; }
  .contact { font-size: 20px; font-weight: 700; }
  .phone { top: 444px; }
  .mobile { top: 471px; }
  .fax { top: 498px; }
  .email { top: 525px; }
  .rule {
    position: absolute; left: 50%; width: 78px; margin-left: -39px;
    height: 3px; background: var(--ink);
  }
  .rule--one { top: 557px; }
  .rule--two { top: 613px; }
  .address { font-size: 16px; font-weight: 700; }
  .addr-mel-1 { top: 567px; }
  .addr-mel-2 { top: 589px; }
  .addr-syd-1 { top: 623px; }
  .addr-syd-2 { top: 645px; }

  .back-brand {
    position: absolute; inset: 0;
    display: flex; flex-direction: column; align-items: center; justify-content: center; gap: 36px;
  }
  .back-square { width: 150px; height: 150px; background: var(--mark-grey); }
  .back-name {
    font-size: 62px; font-weight: 800; line-height: 1;
    color: var(--mark-grey); letter-spacing: -1px;
  }
</style>
</head>
<body>
<div class="canvas">
  <div class="board"></div>

  <section class="card card--front" aria-label="Business card front">
    <h1 class="front-line company-name">Korvanta</h1>
    <p class="front-line tagline">CRM, Mobile &amp; Enterprise solutions</p>

    <div class="brand-block">
      <div class="brand-square"></div>
      <div class="brand-name">Korvanta</div>
    </div>

    <div class="partner">
      <span class="partner-badge" role="img" aria-label="Delvaro certified partner badge"></span>
      <span>Delvaro Certified Partner</span>
    </div>
    <p class="front-line competencies">DV Pellucor CRM &nbsp;|&nbsp; DV Quillnest</p>

    <p class="front-line website">www.korvanta.com.au</p>
    <p class="front-line contact phone">Telephone: 1300 482 617</p>
    <p class="front-line contact mobile">Mobile: 0412 738 205</p>
    <p class="front-line contact fax">FAX: +612 804 3392</p>
    <p class="front-line contact email">info@korvanta.com.au</p>

    <div class="rule rule--one"></div>
    <p class="front-line address addr-mel-1">412 Arden Parade</p>
    <p class="front-line address addr-mel-2">Melbourne, VIC 3000</p>
    <div class="rule rule--two"></div>
    <p class="front-line address addr-syd-1">Level 4, 22 Merrow Street</p>
    <p class="front-line address addr-syd-2">Chatswood, NSW 2067</p>
  </section>

  <section class="card card--back" aria-label="Business card back">
    <div class="back-brand">
      <div class="back-square"></div>
      <div class="back-name">Korvanta</div>
    </div>
  </section>
</div>
</body>
</html>
```